We need a website design for an HVAC (Heating & Air Conditioning) Contractor*

Our HVAC client would like to have a more professional looking site as their current one (https://brisvanecomfortworks.example/) is a template site. We will be building the site in-house from the concept.
Items we'd like to incorporate:
- A banner on the homepage that has a click to call plus a form on the right side of the banner
- There is a video on the current website homepage, please find a place to incorporate this.
- We will need to have at least 800 words of content on the homepage, please find space for that (can be a description of a few of the heating / air conditioning services they do). Feel free to use filler content (lorem ipsum) if need be to just show how the content would look

All submissions must have a homepage and a related subpage concept.

Number of Pages Required

1 page

```html
<!DOCTYPE html>
<html lang="en">
<head>
<meta charset="utf-8">
<title>Brisvane Heat &amp; Air Conditioning</title>
<link href="https://fonts.googleapis.com/css2?family=Poppins:wght@400;500;600&family=Roboto+Condensed:wght@400;500;700&family=PT+Serif:wght@400;700&display=swap" rel="stylesheet">
<style>
:root{
  --navy:#0e2f66;
  --navy-deep:#0b2756;
  --red:#d23132;
  --red-dark:#b8262a;
  --ink:#1d1d1d;
  --muted:#6b6f78;
  --pale:#eef1f6;
  --white:#ffffff;
}
*{box-sizing:border-box;margin:0;padding:0}
html,body{width:1200px;height:3338px;overflow:hidden}
body{font-family:"Poppins",sans-serif;color:var(--ink);background:var(--white);position:relative}
.abs{position:absolute}
.cond{font-family:"Roboto Condensed",sans-serif}
.serif{font-family:"PT Serif",serif}

/* top bar */
.topbar{left:0;top:0;width:1200px;height:36px;background:var(--navy);color:#fff;font-size:12px}
.topbar .welcome{left:61px;top:11px}
.topbar .welcome em{font-style:italic}
.topbar .info{top:11px;display:flex;align-items:center;gap:8px}
.topbar .dot{width:24px;height:24px;border-radius:50%;background:#fff;display:flex;align-items:center;justify-content:center;margin-top:-5px}

/* header */
.header{left:0;top:36px;width:1200px;height:77px;background:#fff}
.brand{left:61px;top:22px;display:flex;align-items:center;gap:8px;font-family:"Roboto Condensed",sans-serif;font-weight:700;font-size:28px;color:var(--red);letter-spacing:1px}
.brand .mark{width:14px;height:14px;background:var(--navy)}
.nav{left:540px;top:33px;display:flex;gap:30px;font-size:12px;color:#444;letter-spacing:.3px}
.nav .active{color:var(--red);position:relative;padding-left:10px}
.nav .active:before{content:"";position:absolute;left:0;top:0;width:3px;height:14px;background:var(--red);transform:skewX(-25deg)}
.nav .active:after{content:"";position:absolute;left:0;right:0;bottom:-3px;height:1px;background:var(--navy)}
.btn{display:flex;align-items:center;justify-content:center;background:var(--red);color:#fff;font-family:"PT Serif",serif;font-size:14px;letter-spacing:.4px;position:absolute}
.btn:after{content:"";position:absolute;right:-12px;top:0;width:7px;height:100%;background:var(--navy);transform:skewX(-20deg)}
.btn.navy{background:var(--navy)}
.btn.navy:after{background:#fff}

/* hero */
.hero{left:0;top:113px;width:1200px;height:636px;background:linear-gradient(100deg,#2f5a8e 0%,#4d76a6 45%,#8aa3bf 100%)}
.hero .shade{left:0;top:0;width:1200px;height:636px;background:linear-gradient(90deg,rgba(22,58,110,.55),rgba(22,58,110,.15))}
.hero-title{left:62px;top:220px;color:#fff}
.hero-title .big{font-family:"Roboto Condensed",sans-serif;font-weight:700;font-size:78px;letter-spacing:1px;line-height:1;display:inline-block}
.hero-title .small{font-family:"PT Serif",serif;font-size:36px;letter-spacing:1px}
.form{left:803px;top:68px;width:336px;height:493px;background:var(--red)}
.form h2{position:absolute;left:0;right:0;top:42px;text-align:center;font-family:"PT Serif",serif;font-weight:400;font-size:19px;color:#fff;letter-spacing:.8px}
.field{position:absolute;left:39px;width:259px;height:33px;background:#fff;border-radius:3px;font-size:12px;color:#777;padding:9px 10px}

/* section headings */
.eyebrow{font-size:13px;font-weight:600;color:#111;text-align:center}
.heading{font-family:"Roboto Condensed",sans-serif;font-weight:500;font-size:24px;color:var(--navy);display:flex;align-items:center;gap:6px}
.heading .r{color:var(--red)}
.heading .slash{width:17px;height:22px;position:relative;margin-right:2px}
.heading .slash:before{content:"";position:absolute;left:8px;top:0;width:3px;height:22px;background:var(--navy);transform:skewX(-30deg)}
.heading .slash:after{content:"";position:absolute;left:0;bottom:0;width:70px;height:2px;background:var(--navy)}

/* services */
.services{left:0;top:749px;width:1200px;height:676px;background:var(--pale);overflow:hidden}
.card{position:absolute;top:162px;width:345px;height:450px;background:#fff;box-shadow:0 3px 12px rgba(20,40,80,.12)}
.card .ph{position:absolute;left:0;top:0;width:345px;height:226px}
.card h3{position:absolute;left:0;right:0;top:250px;text-align:center;font-family:"Roboto Condensed",sans-serif;font-weight:400;font-size:22px}
.card p{position:absolute;left:34px;right:34px;top:288px;text-align:center;font-size:12.3px;line-height:19.5px;color:var(--muted)}
.card .more{position:absolute;left:0;bottom:0;width:345px;height:37px;display:flex;align-items:center;justify-content:space-between;padding:0 20px 0 31px;font-size:12px;font-weight:500;border-top:1px solid #e3e6ea}
.card .more.filled{background:var(--red);color:#fff;border-top:none}
.card .more.plain{color:var(--red)}

/* about */
.about-frame{left:198px;top:1501px;width:250px;height:380px;border:9px solid var(--red);border-right:none;border-bottom:none}
.about-photo{left:207px;top:1507px;width:310px;height:375px;background:linear-gradient(135deg,#9fb2c6,#c9b98a 60%,#6f7f95);clip-path:polygon(0 0,80% 0,100% 16%,100% 100%,0 100%)}
.about-text{left:601px;top:1546px;width:405px}
.about-text p{font-size:12.3px;line-height:19.6px;color:var(--muted);margin-top:10px}

/* video */
.video{left:0;top:1965px;width:1200px;height:450px;background:linear-gradient(100deg,#123a78 0%,#1c4a8a 50%,#123a78 100%)}
.video .overlay{left:0;top:0;width:1200px;height:450px;background:rgba(14,47,102,.55)}
.video .eyebrow{color:#fff}
.play{left:448px;top:224px;width:52px;height:52px;border-radius:50%;background:#fff;box-shadow:0 0 0 6px rgba(255,255,255,.25);display:flex;align-items:center;justify-content:center}

/* testimonials */
.tcard{position:absolute;top:2569px;width:252px;height:289px;background:#fff;box-shadow:0 3px 14px rgba(20,40,80,.12);overflow:hidden}
.tcard .av{position:absolute;left:27px;top:25px;width:48px;height:48px;border-radius:50%;border:3px solid #e6e8ee;background:linear-gradient(135deg,#c9a48a,#8b6a5a)}
.tcard .nm{position:absolute;left:102px;top:32px;font-family:"Roboto Condensed",sans-serif;font-size:15px;color:#111}
.tcard .sv{position:absolute;left:102px;top:52px;font-size:12.5px;color:#444}
.tcard p{position:absolute;left:17px;width:215px;top:112px;font-size:12px;line-height:19.5px;color:var(--muted)}
.tcard svg{position:absolute;left:0;top:0}

/* footer */
.footer{left:0;top:2994px;width:1200px;height:344px;background:var(--navy);color:#fff;overflow:hidden}
.footer h4{position:absolute;top:60px;font-family:"Roboto Condensed",sans-serif;font-weight:400;font-size:21px}
.footer ul{position:absolute;top:105px;list-style:none;font-size:12.3px;line-height:27px;color:#dbe3f0}
.fcontact{position:absolute;left:889px;display:flex;gap:8px;font-size:12.3px;line-height:19.5px;color:#dbe3f0}
.ficon{width:28px;height:28px;border-radius:4px;background:#fff;display:flex;align-items:center;justify-content:center;flex:none}
</style>
</head>
<body>

<div class="abs topbar">
  <div class="abs welcome">Welcome To <em>BRISVANE!</em></div>
  <div class="abs info" style="left:675px">
    <span class="dot"><svg width="14" height="14" viewBox="0 0 14 14"><circle cx="7" cy="7" r="5.5" fill="none" stroke="#d23132" stroke-width="1.6"/><path d="M7 4v3.3l2 1.3" fill="none" stroke="#d23132" stroke-width="1.4"/></svg></span>
    <span>Opening Hours &nbsp;: 8:00 Am To 5:00pm</span>
  </div>
  <div class="abs info" style="left:976px">
    <span class="dot"><svg width="13" height="13" viewBox="0 0 24 24"><path fill="#d23132" d="M6.6 10.8a15 15 0 006.6 6.6l2.2-2.2a1 1 0 011-.25 11.4 11.4 0 003.6.6 1 1 0 011 1V20a1 1 0 01-1 1A17 17 0 013 4a1 1 0 011-1h3.5a1 1 0 011 1c0 1.25.2 2.45.6 3.6a1 1 0 01-.25 1z"/></svg></span>
    <span>Call Us : 555 010 2846</span>
  </div>
</div>

<header class="abs header">
  <div class="abs brand"><span class="mark"></span>BRISVANE</div>
  <nav class="abs nav">
    <span class="active">HOME</span><span>ABOUT US</span><span>SERVICE</span><span>TESTIMONIALS</span><span>CONTACT US</span>
  </nav>
  <div class="btn" style="left:989px;top:21px;width:134px;height:36px">CALL US NOW</div>
</header>

<section class="abs hero">
  <div class="abs" role="img" aria-label="Photo of a technician in a blue cap servicing a wall-mounted air conditioner" style="left:0;top:0;width:1200px;height:636px"></div>
  <div class="abs shade"></div>
  <div class="abs hero-title">
    <div><span class="big">BRISVANE</span><span class="small"> HEAT &amp; AIR</span></div>
    <div class="small" style="margin-top:4px">CONDITIONING</div>
  </div>
  <div class="btn" style="left:60px;top:386px;width:190px;height:36px">BOOK AN APPOINTMENT</div>
  <div class="abs form">
    <h2>SUBMIT A REQUEST</h2>
    <div class="field" style="top:94px">Name*</div>
    <div class="field" style="top:139px">Email*</div>
    <div class="field" style="top:184px">Phone no*</div>
    <div class="field" style="top:227px">Service*<svg class="abs" style="right:11px;top:14px" width="12" height="7"><path d="M0 0h12L6 7z" fill="#d23132"/></svg></div>
    <div class="field" style="top:272px;height:60px">Description</div>
    <div class="field" style="top:343px;height:37px;padding-top:11px">dd/mm/yy<svg class="abs" style="right:9px;top:10px" width="16" height="16" viewBox="0 0 16 16"><rect x="1" y="3" width="14" height="12" fill="none" stroke="#e08a8a" stroke-width="1.4"/><path d="M1 6h14M5 1v4M11 1v4M4 9h8M4 12h8" stroke="#e08a8a" stroke-width="1.2"/></svg></div>
    <div class="btn navy" style="left:67px;top:397px;width:186px;height:36px">BOOK AN APPOINTMENT</div>
  </div>
</section>

<section class="abs services">
  <svg class="abs" style="left:0;top:0" width="1200" height="676"><path d="M0 200 L330 676 H0Z" fill="#e4e8ef"/><path d="M620 676 L900 330 L1200 330 V676Z" fill="#e7ebf1"/></svg>
  <div class="abs eyebrow" style="left:0;width:1200px;top:76px">What We Do</div>
  <div class="abs heading" style="left:476px;top:101px"><span class="slash"></span><span class="r">SERVICE</span> WE PROVIDE</div>
  <div class="card" style="left:214px">
    <div class="ph" role="img" aria-label="Photo of a technician repairing a furnace control panel" style="background:linear-gradient(120deg,#d9dde2,#8a6f66 55%,#3d4d6b)"></div>
    <h3>Heating Service</h3>
    <p>Lorem Ipsum is simply dummy text of the printing and typesetting industry. Lorem Ipsum has been the industry's standard dummy text ever since the 1500s, when an unknown printer took a galley of type and scrambled it</p>
    <div class="more filled"><span>READ MORE</span><svg width="18" height="14" viewBox="0 0 18 14"><path d="M1 7h15M10 1l6 6-6 6" fill="none" stroke="#fff" stroke-width="1.6"/></svg></div>
  </div>
  <div class="card" style="left:596px">
    <div class="ph" role="img" aria-label="Photo of a technician checking an outdoor air conditioning unit with gauges" style="background:linear-gradient(120deg,#e6e8eb,#c3c8cf 45%,#3a7fc4)"></div>
    <h3>Air Conditioning</h3>
    <p>Lorem Ipsum is simply dummy text of the printing and typesetting industry. Lorem Ipsum has been the industry's standard dummy text ever since the 1500s,when an unknown printer took a galley of type and scrambled it</p>
    <div class="more plain"><span>READ MORE</span><svg width="18" height="14" viewBox="0 0 18 14"><path d="M1 7h15M10 1l6 6-6 6" fill="none" stroke="#d23132" stroke-width="1.6"/></svg></div>
  </div>
</section>

<div class="abs about-frame"></div>
<div class="abs about-photo" role="img" aria-label="Photo of a smiling technician in a yellow hard hat beside an outdoor unit"></div>
<div class="abs about-text">
  <div class="eyebrow" style="text-align:left">Who We Are</div>
  <div class="heading" style="margin-top:12px"><span class="slash"></span><span class="r">ABOUT</span>&nbsp;US</div>
  <p>Lorem Ipsum is simply dummy text of the printing and typesetting industry. Lorem Ipsum has been the industry's standard dummy text ever since the 1500s,when an unknown printer took a galley of type and scrambled it</p>
  <p>Lorem Ipsum is simply dummy text of the printing and typesetting industry. Lorem Ipsum has been the industry's standard dummy text ever since the 1500s,when an unknown printer took a galley of type and scrambled it</p>
</div>
<div class="btn" style="left:600px;top:1797px;width:137px;height:37px">LEARN MORE</div>
<svg class="abs" style="left:0;top:1890px" width="1200" height="76"><path d="M760 76 C950 60 1100 30 1200 2 V76Z" fill="var(--red)"/><path d="M900 76 C1020 55 1120 28 1200 8 V0 C1100 28 980 58 900 76Z" fill="var(--navy)"/></svg>

<section class="abs video">
  <div class="abs" role="img" aria-label="Background photo of a man relaxing on a sofa beside a houseplant" style="left:0;top:0;width:1200px;height:450px"></div>
  <div class="abs overlay"></div>
  <div class="abs eyebrow" style="left:0;width:1200px;top:76px">Our History</div>
  <div class="abs heading" style="left:530px;top:104px;color:#fff"><span class="slash" style="filter:brightness(0) invert(1)"></span><span class="r">Whatch</span> Vedio</div>
  <p class="abs" style="left:298px;top:153px;width:604px;text-align:center;font-size:12.3px;line-height:19.6px;color:#cfd9ea">Lorem Ipsum is simply dummy text of the printing and typesetting industry. Lorem Ipsum has been the industry's standard dummy text ever since the 1500s, when an unknown printer took a galley of type and scrambled it</p>
  <div class="abs play"><svg width="18" height="18" viewBox="0 0 18 18"><circle cx="9" cy="9" r="9" fill="var(--red)"/><path d="M7 5l6 4-6 4z" fill="#fff"/></svg></div>
  <div class="abs cond" style="left:522px;top:239px;font-size:18px;color:#fff">Don't Know What To Start With?</div>
  <div class="abs cond" style="left:0;width:1200px;top:292px;text-align:center;font-size:29px;font-weight:500;color:#fff;line-height:45px">Get A Solutions For All<br>Home Services</div>
</section>

<section class="testi">
  <div class="abs eyebrow" style="left:0;width:1170px;top:2489px;color:#111">Testimonials</div>
  <div class="abs heading" style="left:462px;top:2516px"><span class="slash"></span><span class="r">WHAT OUR</span> CUSTOMER SAY</div>
</section>

<div class="tcard" style="left:60px">
  <svg width="252" height="289"><path d="M252 186 C238 250 180 282 108 289 H252Z" fill="var(--red)"/></svg>
  <div class="av" role="img" aria-label="Customer portrait"></div>
  <div class="nm">-&nbsp; Customer Name</div><div class="sv">Service Name</div>
  <p>Lorem Ipsum is simply dummy text of the printing and typesetting industry. Lorem Ipsum has been the industry's standard dummy text ever since the 1500s, when an unknown printer took a galley of type and scrambled it</p>
</div>
<div class="tcard" style="left:336px">
  <svg width="252" height="289"><path d="M0 0 H252 C150 10 60 60 0 130Z" fill="var(--navy)"/><path d="M252 186 C238 250 180 282 108 289 H252Z" fill="var(--red)"/></svg>
  <div class="av" role="img" aria-label="Customer portrait" style="background:linear-gradient(135deg,#6b4a3c,#2f2320)"></div>
  <div class="nm">-&nbsp; Customer Name</div><div class="sv">Service Name</div>
  <p>Lorem Ipsum is simply dummy text of the printing and typesetting industry. Lorem Ipsum has been the industry's standard dummy text ever since the 1500s, when an unknown printer took a galley of type and scrambled it</p>
</div>
<div class="tcard" style="left:610px">
  <svg width="252" height="289"><path d="M252 186 C238 250 180 282 108 289 H252Z" fill="var(--red)"/></svg>
  <div class="av" role="img" aria-label="Customer portrait" style="background:linear-gradient(135deg,#8fa3b8,#3f5a78)"></div>
  <div class="nm">-&nbsp; Customer Name</div><div class="sv">Service Name</div>
  <p>Lorem Ipsum is simply dummy text of the printing and typesetting industry. Lorem Ipsum has been the industry's standard dummy text ever since the 1500s, when an unknown printer took a galley of type and scrambled it</p>
</div>
<div class="tcard" style="left:886px">
  <svg width="252" height="289"><path d="M252 186 C238 250 180 282 108 289 H252Z" fill="var(--red)"/></svg>
  <div class="av" role="img" aria-label="Customer portrait" style="background:linear-gradient(135deg,#d9b3a8,#9a4a55)"></div>
  <div class="nm">-&nbsp; Customer Name</div><div class="sv">Service Name</div>
  <p>Lorem Ipsum is simply dummy text of the printing and typesetting industry. Lorem Ipsum has been the industry's standard dummy text ever since the 1500s, when an unknown printer took a galley of type and scrambled it</p>
</div>
<div class="btn" style="left:525px;top:2881px;width:134px;height:36px">VIEW MORE</div>

<footer class="abs footer">
  <div class="abs brand" style="top:66px;left:61px"><span class="mark" style="background:var(--red)"></span><span style="color:#fff">BRISVANE</span></div>
  <p class="abs" style="left:61px;top:131px;width:240px;font-size:12.3px;line-height:19.6px;color:#dbe3f0">Lorem Ipsum is simply dummy text of the printing and typesetting industry. Lorem Ipsum has been the industry's standard dummy text ever since the 1500s, when an unknown printer took a galley of type and scrambled it</p>
  <h4 style="left:337px">Quick Link</h4>
  <ul style="left:337px"><li>- Home</li><li>- About Us</li><li>- Services</li><li>- Testimonials</li><li>- Contact Us</li></ul>
  <h4 style="left:613px">Information</h4>
  <ul style="left:613px"><li>- Privacy</li><li>- Terms of service</li><li>- Terms of Use</li><li>- Help</li><li>- Legal</li></ul>
  <h4 style="left:889px">Contact Us</h4>
  <div class="fcontact" style="top:98px"><span class="ficon"><svg width="14" height="18" viewBox="0 0 14 18"><path d="M7 0a7 7 0 00-7 7c0 5 7 11 7 11s7-6 7-11a7 7 0 00-7-7z" fill="var(--red)"/><circle cx="7" cy="7" r="2.6" fill="#fff"/></svg></span><span style="width:200px">Lorem Ipsum is simply dummy text of the printing</span></div>
  <div class="fcontact" style="top:168px"><span class="ficon"><svg width="15" height="15" viewBox="0 0 24 24"><path fill="var(--red)" d="M6.6 10.8a15 15 0 006.6 6.6l2.2-2.2a1 1 0 011-.25 11.4 11.4 0 003.6.6 1 1 0 011 1V20a1 1 0 01-1 1A17 17 0 013 4a1 1 0 011-1h3.5a1 1 0 011 1c0 1.25.2 2.45.6 3.6a1 1 0 01-.25 1z"/></svg></span><span style="padding-top:2px">555 010 2846</span></div>
  <div class="fcontact" style="top:242px"><span class="ficon"><svg width="16" height="12" viewBox="0 0 16 12"><rect width="16" height="12" fill="var(--red)"/><path d="M0 0l8 6 8-6" fill="none" stroke="#fff" stroke-width="1.4"/></svg></span><span style="padding-top:4px">info@brisvanecomfort.example</span></div>
  <svg class="abs" style="left:0;top:244px" width="1200" height="100"><path d="M0 10 C200 40 420 85 600 100 H0Z" fill="var(--red)"/></svg>
  <div class="abs" style="left:61px;top:322px;font-size:11.5px;color:#fff">©Copy right BRISVANE2021-All Right Reserved.</div>
</footer>

</body>
</html>
```